Norvane Structural Approval Standards Private Assessors

Professional Construction Consultancy Company Business Card - must keep logo colours see images below - examples have been added from my last competition - please see them as examples only!

Target Market(s)

Home Builders

Industry/Entity Type

Construction

Contact Information for Business Card

See "must haves"

Font styles to use
Sans Serif

Colors
ffffff
add136
000000

Requirements
Must have
• Daniel Moravi
• Director
• Phone: 0431 587 219
• Address: 7 Tarrunga Rd,
• Hallworth Vale, SA, 5091
• Email: norvane@mailbox-example.com
• Website: www.norvane-example.com.au
• Facebook: Norvane Structural Approval Standards
Nice to have
• Side 1: full logo
• Side 2: company details
Should not have
• hard to read
• must be clear and professional

```html
<!DOCTYPE html>
<html lang="en">
<head>
<meta charset="utf-8">
<title>Norvane Structural Approval Standards – Business Card</title>
<link rel="stylesheet" href="https://fonts.googleapis.com/css2?family=Montserrat:wght@600;700&family=Roboto:wght@400;500&display=swap">
<style>
  :root {
    --white: #ffffff;
    --green: #add136;
    --black: #000000;
    --ink: #2a2a2a;
    --backdrop: #dcdcdc;
  }
  * { box-sizing: border-box; margin: 0; padding: 0; }
  html, body { width: 1200px; height: 1200px; overflow: hidden; }
  body {
    background: var(--backdrop);
    font-family: "Roboto", Arial, sans-serif;
    display: flex;
    flex-direction: column;
    align-items: center;
    justify-content: center;
    gap: 60px;
  }
  .card {
    position: relative;
    width: 840px;
    height: 480px;
    background: var(--white);
    border-radius: 36px;
    overflow: hidden;
    box-shadow: 0 6px 18px rgba(0,0,0,0.12);
  }
  .card-band {
    position: absolute;
    left: 0; right: 0; bottom: 0;
    height: 66px;
    background: var(--black);
    border-top: 8px solid var(--green);
    display: flex;
    align-items: center;
    justify-content: center;
    color: var(--white);
    font-size: 17px;
    letter-spacing: 2.5px;
  }
  .brand {
    display: flex;
    align-items: center;
    gap: 16px;
    font-family: "Montserrat", Arial, sans-serif;
    font-weight: 700;
    color: var(--green);
  }
  .brand-mark { background: var(--green); flex: none; }
  .brand-name { line-height: 1.15; text-transform: uppercase; }

  /* front */
  .card-front .brand {
    position: absolute;
    left: 50%; top: 200px;
    transform: translate(-50%, -50%);
  }
  .card-front .brand-mark { width: 70px; height: 70px; }
  .card-front .brand-name { font-size: 30px; width: 470px; }

  /* back */
  .card-back .brand {
    position: absolute;
    left: 50px; top: 48px;
  }
  .card-back .brand-mark { width: 34px; height: 34px; }
  .card-back .brand-name { font-size: 14px; width: 270px; }

  .person { position: absolute; left: 70px; top: 200px; }
  .person-name {
    font-family: "Montserrat", Arial, sans-serif;
    font-weight: 700;
    font-size: 36px;
    color: var(--green);
  }
  .person-role { font-size: 17px; color: var(--ink); letter-spacing: 1px; margin-top: 4px; }

  .divider {
    position: absolute;
    left: 70px; right: 60px; top: 300px;
    height: 2px;
    background: var(--green);
  }
  .address {
    position: absolute;
    left: 70px; top: 320px;
    font-size: 17px;
    line-height: 1.6;
    color: var(--ink);
    letter-spacing: 1px;
  }
  .contact-list {
    position: absolute;
    right: 60px; top: 176px;
    list-style: none;
    font-size: 17px;
    color: var(--ink);
    letter-spacing: 0.8px;
  }
  .contact-list li {
    display: flex;
    align-items: center;
    gap: 12px;
    line-height: 1.85;
  }
  .contact-icon { width: 18px; height: 18px; flex: none; }
</style>
</head>
<body>

  <section class="card card-front" aria-label="Business card front">
    <div class="brand">
      <span class="brand-mark"></span>
      <span class="brand-name">Norvane Structural Approval Standards Private Assessors</span>
    </div>
    <div class="card-band">www.norvane-example.com.au</div>
  </section>

  <section class="card card-back" aria-label="Business card back">
    <div class="brand">
      <span class="brand-mark"></span>
      <span class="brand-name">Norvane Structural Approval Standards Private Assessors</span>
    </div>

    <div class="person">
      <p class="person-name">Daniel Moravi</p>
      <p class="person-role">director</p>
    </div>

    <ul class="contact-list">
      <li>
        <svg class="contact-icon" viewBox="0 0 18 18" aria-hidden="true"><rect x="4" y="1.5" width="10" height="15" rx="2" fill="none" stroke="#000" stroke-width="1.8"/></svg>
        0431 587 219
      </li>
      <li>
        <svg class="contact-icon" viewBox="0 0 18 18" aria-hidden="true"><rect x="1.5" y="3.5" width="15" height="11" rx="1.5" fill="none" stroke="#add136" stroke-width="1.8"/><path d="M2 4.5 L9 10 L16 4.5" fill="none" stroke="#add136" stroke-width="1.8"/></svg>
        norvane@mailbox-example.com
      </li>
      <li>
        <svg class="contact-icon" viewBox="0 0 18 18" aria-hidden="true"><rect x="2" y="2" width="14" height="14" rx="2" fill="#add136"/></svg>
        Norvane Structural Approval Standards
      </li>
    </ul>

    <div class="divider"></div>

    <p class="address">7 Tarrunga Rd,<br>Hallworth Vale, SA, 5091</p>

    <div class="card-band">www.norvane-example.com.au</div>
  </section>

</body>
</html>
```